First and Only Single Serving Dental Tooth Powder Company NEEDS Packaging DESIGN

We need a packaging design for a new company based in Florida called 'BrisoTin'. We created the first and only single serving dental tooth powder, for use with or without water. This solves a world problem in numerous faucets. Our product is great for Travelers, Adventure Seekers, Military Personnel, Daily Commuters and any one else wanting the cleanest mouth and freshest breath.

- This is a front and back of a 4(four) by 6(six) package design needed

Target Market(s)

Travelers,Outdoorsman, Adventure seekers, Daily Commuters, and Military Personnel.

Industry/Entity Type

Dental

Requirements
Must have
• -This must fit a package with the dimensions of 4" x 6"
• -four inches by six inches.
• -Earthy/Naturalistic Appeal
• - This is a front and back of a 4(four) by 6(six) package design needed
• -The package will be a White Nylon/Mylar bag
Nice to have
• -Clean your teeth anywhere, anytime...
• -Clean, Compact, Dependable
• -BrisoTin activates without water
• -Proudly made in the USA.
• -Package contains 15 BrisoTin's.
• -The Flavor for the BrisoTin is "Tripple Berry"
• -BrisoTin is for the everyday person on-the-go.
• -Our Story..
• Brisotin was brought to life for moments when time is vital and packing light is a must. We were tired of the same old ordinary way of cleaning our teeth while outdoors, on our adventures, or traveling the globe. The old way required water for it's use which isn't always readily available. With BrisoTin, water is not necessary. The package you hold in your hand contains no ordinary product. In fact, the way you use it is extremely unique and simple.
• Directions: Rip, Pour, Swish, Dispense. Enjoy your adventure responsibly!
Should not have
• A bunch of clutter besides that I am open to ideas.

```html
<!DOCTYPE html>
<html lang="en">
<head>
<meta charset="utf-8">
<title>BrisoTin Dental Tooth Powder – Pouch Designs</title>
<link href="https://fonts.googleapis.com/css2?family=Didact+Gothic&family=Roboto+Condensed:ital,wght@0,400;0,600;1,400&display=swap" rel="stylesheet">
<style>
  :root{
    --bg:#ffffff;
    --pouch-white:#f4f3f1;
    --pouch-shade:#dcdbd8;
    --seal-line:#c9c8c5;
    --mint:#79c29c;
    --green-dark:#4f7f2c;
    --green:#6a9a3e;
    --green-light:#a3cc6a;
    --tan-dark:#9a5a3a;
    --tan:#c8895d;
    --tan-light:#e6bd8a;
    --plum-dark:#3f1636;
    --plum:#7a2570;
    --magenta:#c23cb2;
    --cream:#f2ebe3;
    --badge:#d9c9a8;
  }
  *{box-sizing:border-box;margin:0;padding:0}
  html,body{width:1200px;height:900px;overflow:hidden;background:var(--bg)}
  body{position:relative;font-family:"Roboto Condensed",sans-serif}

  .pouch{position:absolute;top:150px;width:320px;height:600px;overflow:hidden;
    border-radius:3px;box-shadow:0 14px 30px rgba(0,0,0,.12)}
  .pouch--green{left:200px}
  .pouch--berry{left:680px}

  .pouch__top{position:absolute;top:0;left:0;right:0;height:224px;
    background:linear-gradient(180deg,var(--pouch-shade) 0%,var(--pouch-white) 30%,#fff 60%,var(--pouch-white) 100%)}
  .seal{position:absolute;left:0;right:0;height:2px;background:var(--seal-line)}
  .seal--a{top:40px}.seal--b{top:86px}

  .brand{position:absolute;top:122px;left:0;right:0;display:flex;flex-direction:column;align-items:center;gap:8px}
  .brand__dot{width:26px;height:26px;border-radius:50%;background:var(--mint)}
  .brand__name{font-weight:600;font-size:30px;letter-spacing:1px;color:var(--mint)}

  .tagline{position:absolute;top:224px;left:0;right:0;height:26px;
    display:flex;align-items:center;justify-content:center;
    font-style:italic;font-size:17px;color:var(--cream)}
  .pouch--green .tagline{background:var(--green)}
  .pouch--berry .tagline{background:var(--magenta)}

  .title-band{position:absolute;top:250px;left:0;right:0;height:96px;
    background:linear-gradient(90deg,var(--tan-dark) 0%,var(--tan) 45%,var(--tan-light) 100%);
    display:flex;align-items:center;justify-content:center;text-align:center}
  .title{font-family:"Didact Gothic",sans-serif;font-weight:400;font-size:35px;line-height:1.08;color:var(--cream)}

  .lower{position:absolute;top:346px;left:0;right:0;bottom:0}
  .pouch--green .lower{background:linear-gradient(90deg,var(--green-dark),var(--green))}
  .pouch--berry .lower{background:linear-gradient(90deg,var(--plum-dark),var(--plum) 60%,var(--magenta))}
  .lower__shape{position:absolute;inset:0}

  .usage{position:absolute;top:10px;left:0;right:0;text-align:center;font-size:19px;color:var(--cream)}
  .claims{position:absolute;left:60px;right:30px;text-align:center;color:var(--cream);font-style:italic}
  .claim{font-size:18px;line-height:1.1;margin-bottom:12px}
  .flavor{display:flex;align-items:center;justify-content:center;gap:6px;font-size:12px;margin-bottom:10px}
  .flavor__icon{width:16px;height:16px;border-radius:50%;border:2px solid var(--cream)}
  .pouch--berry .flavor__text{background:var(--magenta);padding:2px 6px}
  .pouch--berry .flavor__icon{border-color:var(--plum)}
  .contents{font-size:13px}
  .pouch--green .claims{top:104px}
  .pouch--berry .claims{top:96px}
  .origin-badge{position:absolute;right:8px;bottom:40px;width:26px;height:26px;border-radius:50%;
    background:var(--badge);border:2px solid var(--cream)}
</style>
</head>
<body>

<div class="pouch pouch--green">
  <div class="pouch__top">
    <span class="seal seal--a"></span><span class="seal seal--b"></span>
    <div class="brand"><span class="brand__dot"></span><span class="brand__name">BRISOTIN</span></div>
  </div>
  <div class="tagline">Clean, Compact, Dependable</div>
  <div class="title-band"><h1 class="title">DENTAL TOOTH<br>POWDER</h1></div>
  <div class="lower">
    <svg class="lower__shape" viewBox="0 0 320 254" preserveAspectRatio="none">
      <defs><radialGradient id="domeGreen" cx="0.6" cy="0.2" r="0.8">
        <stop offset="0" stop-color="#a3cc6a"/><stop offset="1" stop-color="#6a9a3e"/></radialGradient></defs>
      <path d="M50 254 Q110 70 250 44 Q305 80 320 170 L320 254 Z" fill="url(#domeGreen)" opacity=".85"/>
    </svg>
    <p class="usage">For use with or without water</p>
    <div class="claims">
      <p class="claim">activates without water</p>
      <p class="claim">for the everyday<br>person on-the-go</p>
      <p class="flavor"><span class="flavor__icon"></span><span class="flavor__text">Wild Bramble Flavor</span></p>
      <p class="contents">Package includes 30 stick packs.</p>
    </div>
    <span class="origin-badge"></span>
  </div>
</div>

<div class="pouch pouch--berry">
  <div class="pouch__top">
    <span class="seal seal--a"></span><span class="seal seal--b"></span>
    <div class="brand"><span class="brand__dot"></span><span class="brand__name">BRISOTIN</span></div>
  </div>
  <div class="tagline">Clean, Compact, Dependable</div>
  <div class="title-band"><h1 class="title">DENTAL TOOTH<br>POWDER</h1></div>
  <div class="lower">
    <svg class="lower__shape" viewBox="0 0 320 254" preserveAspectRatio="none">
      <defs><linearGradient id="domeTan" x1="0" y1="0" x2="1" y2="0">
        <stop offset="0" stop-color="#9a5a3a"/><stop offset=".5" stop-color="#c8895d"/><stop offset="1" stop-color="#e6bd8a"/></linearGradient></defs>
      <path d="M0 236 Q70 90 200 48 Q290 90 320 190 L320 254 L0 254 Z" fill="url(#domeTan)"/>
    </svg>
    <p class="usage">For use with or without water</p>
    <div class="claims">
      <p class="claim">for the everyday<br>person on-the-go</p>
      <p class="claim">activates without water</p>
      <p class="flavor"><span class="flavor__icon"></span><span class="flavor__text">Wild Bramble Flavor</span></p>
      <p class="contents">Package includes 30 stick packs.</p>
    </div>
    <span class="origin-badge"></span>
  </div>
</div>

</body>
</html>
```